Bright Dabs - Face Painting Company requires business card design

Hi,
I am wanting a business card design for a new business in Brisbane (Australia) called 'Bright Dabs'. We are a childrens face painting company.

I want to communicate a corporate, simple and clean message through my business card, but also fun and relevant to children.

My company colours are black, yellow and purple, and at the moment I am running with a "cheeky smile" type theme, along the lines of the Marchwood Fox (Tobin in Farrowvale).

I want this to look Corporate, clean and simple. On the back I would like to see some creative flair with a border or background design, perhaps in white or another colour.

Requirements
Must have
• Front:
Bright Dabs
Face Painting Designs

Back:
Maren Lockwell
Artist
0491 283 516
maren@brightdabs.com.au
www.brightdabs.com.au
Nice to have
• Attached is the banner which i had made, the business card should go along with this type of theme.
I would like to use the colours Yellow, Black and Purple. Purple should be used in a miniml way, with yellow and black as the main colours.
I want it to have a CORPORATE look.

A Playfull but readable text.

I would like a mix up of the colours on the back in the text.
Maren Lockwell (black)
Artist(purple) etc.

```html
<!DOCTYPE html>
<html lang="en">
<head>
<meta charset="utf-8">
<title>Bright Dabs – Business Card</title>
<link rel="stylesheet" href="https://fonts.googleapis.com/css2?family=Jost:wght@300;400;600&family=Kaushan+Script&display=swap">
<style>
  :root {
    --page: #ecebe6;
    --yellow: #f2ec4f;
    --yellow-light: #f8f4a6;
    --white: #ffffff;
    --black: #111111;
    --purple: #7b3f98;
    --accent-dot: #f2d21b;
  }
  html, body {
    margin: 0;
    padding: 0;
    width: 1200px;
    height: 798px;
    overflow: hidden;
    background: var(--page);
  }
  h1, h2, p { margin: 0; }
  .canvas {
    position: relative;
    width: 1200px;
    height: 798px;
  }
  .card {
    position: absolute;
    border-radius: 30px;
    overflow: hidden;
  }

  /* Front */
  .card-front {
    left: 106px;
    top: 50px;
    width: 564px;
    height: 336px;
    background: var(--yellow);
  }
  .card-front .swirl-area {
    position: absolute;
    right: 0;
    top: 0;
    width: 320px;
    height: 100%;
    background: linear-gradient(110deg, var(--yellow) 0%, var(--yellow-light) 100%);
  }
  .card-front .brand {
    position: absolute;
    left: 0;
    right: 0;
    top: 112px;
    text-align: center;
    font-family: "Jost", sans-serif;
    font-weight: 600;
    font-size: 64px;
    line-height: 1;
    letter-spacing: 1px;
    text-transform: uppercase;
    color: var(--black);
  }
  .card-front .tagline {
    position: absolute;
    left: 0;
    right: 0;
    top: 188px;
    text-align: center;
    font-family: "Jost", sans-serif;
    font-weight: 400;
    font-size: 32px;
    line-height: 1;
    color: var(--black);
  }

  /* Back */
  .card-back {
    left: 546px;
    top: 408px;
    width: 550px;
    height: 336px;
    background: var(--white);
  }
  .card-back .name {
    position: absolute;
    left: 0;
    right: 0;
    top: 100px;
    text-align: center;
    font-family: "Jost", sans-serif;
    font-weight: 300;
    font-size: 61px;
    line-height: 1;
    color: var(--black);
  }
  .card-back .role {
    position: absolute;
    left: 208px;
    top: 160px;
    font-family: "Kaushan Script", cursive;
    font-size: 54px;
    line-height: 1;
    color: var(--purple);
  }
  .card-back .contact-band {
    position: absolute;
    left: 0;
    right: 0;
    bottom: 0;
    height: 56px;
    background: var(--purple);
    display: flex;
    align-items: center;
    justify-content: center;
    gap: 8px;
    font-family: "Jost", sans-serif;
    font-weight: 400;
    font-size: 16px;
    color: var(--white);
  }
  .contact-band .sep {
    width: 5px;
    height: 5px;
    border-radius: 50%;
    background: var(--accent-dot);
  }
</style>
</head>
<body>
<main class="canvas">
  <section class="card card-front">
    <div class="swirl-area" role="img" aria-label="White flowing swirl ornament with small dots"></div>
    <h1 class="brand">Bright Dabs</h1>
    <p class="tagline">Face Painting Designs</p>
  </section>

  <section class="card card-back">
    <h2 class="name">Maren Lockwell</h2>
    <p class="role">Artist</p>
    <div class="contact-band">
      <span class="phone">0491 283 516</span>
      <span class="sep"></span>
      <span class="email">maren@brightdabs.com.au</span>
      <span class="sep"></span>
      <span class="web">www.brightdabs.com.au</span>
    </div>
  </section>
</main>
</body>
</html>
```